Lomi Lomi Business
Zielgruppe
Lomi Lomi Massage /Wellnessmassage
Aufgabenstellung
Design, Farbgebung und Maße bitte angelehnt an das Velkaro-Design #22
Format 10,5x21cm Querformat (DIN Lang plus beim Anbieter "Prospektwelle" genannt)
Texte siehe Anhang
Daten bitte in editierbarem Illustrator, oder InDesign-Format

```html
<!DOCTYPE html>
<html lang="de">
<head>
<meta charset="utf-8">
<title>Hawaiianische Massage &amp; Körperarbeit – Flyer</title>
<link rel="stylesheet" href="https://fonts.googleapis.com/css2?family=PT+Sans:ital,wght@0,400;0,700;1,400&family=Tinos&display=swap">
<style>
  :root{
    --green:#8cba55;
    --green-text:#7aa83f;
    --brown:#7b5420;
    --brown-text:#86591e;
    --ink:#1c1c1c;
    --paper:#ffffff;
    --frame:#8a8a8a;
    --panel:rgba(243,236,229,.9);
  }
  *{margin:0;padding:0;box-sizing:border-box}
  html,body{width:849px;height:1200px;overflow:hidden;background:var(--paper)}
  body{position:relative;font-family:"PT Sans",Arial,sans-serif;color:var(--ink)}
  .sheet-label{position:absolute;left:51px;top:62px;font-family:"Tinos",serif;font-size:16px}

  .card{position:absolute;left:51px;width:769px;border:1px solid var(--frame);overflow:hidden;background:var(--paper)}
  .card--front{top:190px;height:363px}
  .card--back{top:635px;height:378px}

  .photo-bg{position:absolute;inset:0;
    background:linear-gradient(180deg,#f4f1ee 0%,#e8d8cd 25%,#d4a482 55%,#bb7a52 80%,#aa6a43 100%);}

  /* Wordmark: one colour, one weight of the text font */
  .brand{color:var(--brown-text);font-weight:400;line-height:1.1}
  .brand__owner{font-size:15px;letter-spacing:.05em}
  .brand__service{font-size:20px;letter-spacing:.05em;margin-top:8px}

  .title-panel{position:absolute;left:552px;top:17px;width:196px;height:133px;background:var(--panel);
    border-radius:0 40px 0 40px;padding:13px 0 0 18px}

  .badge{position:absolute;color:#fff}
  .badge--opening{left:438px;top:122px;width:124px;height:75px;background:var(--green);border-radius:0 30px 0 30px;padding:14px 0 0 8px;font-size:19px;line-height:1.05}
  .badge--opening span{display:block;padding-left:17px}
  .offer{width:137px;height:115px;top:234px;padding:8px 0 0 10px;border-radius:0 50px 0 50px}
  .offer--lomi{left:29px;background:var(--green)}
  .offer--business{left:175px;background:var(--brown)}
  .offer__title{font-size:15px;letter-spacing:.08em;line-height:1.2}
  .offer__price{font-size:10px;margin-top:1px}
  .offer__price b{font-weight:400;font-size:13px}
  .offer__note{font-size:10px;line-height:1.3;padding-left:26px;margin-top:5px}

  .promo-lead{position:absolute;left:331px;top:262px;color:#fff;font-size:17px}
  .voucher{position:absolute;width:115px;height:60px;border:1px solid;border-radius:0 28px 0 28px;
    font-style:italic;text-align:center;font-size:13.5px;line-height:.98;padding-top:8px}
  .voucher--front{left:331px;top:289px;border-color:rgba(255,255,255,.8);color:#fff}

  .intro{position:absolute;left:26px;top:22px;width:415px}
  .intro__pre{font-size:12.5px}
  .intro__title{color:var(--green-text);font-size:24px;letter-spacing:.06em;margin-top:2px;line-height:1.1}
  .intro__title small{color:var(--ink);font-size:11.5px;letter-spacing:0}
  .intro p{font-size:11.5px;line-height:17px}
  .intro p+p{margin-top:11px}

  .logo-block{position:absolute;left:465px;top:16px}
  .portrait{position:absolute;left:652px;top:16px;width:112px;height:143px;border-radius:14px 14px 0 0;
    background:linear-gradient(180deg,#d9b88c 0%,#cfae80 70%,#2a2a2a 100%)}
  .bio{position:absolute;right:12px;top:165px;text-align:right;font-size:10.5px;line-height:14.5px}
  .bio__name{font-size:13.5px;font-weight:700;line-height:18px}

  .reminder{position:absolute;left:465px;top:248px;color:var(--brown-text);font-size:12.5px}
  .voucher--back{left:465px;top:268px;width:118px;height:61px;border-color:var(--green);color:var(--green-text)}
  .appointments{position:absolute;left:594px;top:318px;color:var(--brown-text);font-size:12px}
  .bamboo{position:absolute;left:0;top:222px;width:404px;height:148px;
    background:radial-gradient(ellipse 210px 60px at 210px 70px,#4f9630 0%,#86c05e 50%,rgba(255,255,255,0) 80%)}
  .contact{position:absolute;right:12px;top:346px;font-size:13px;letter-spacing:.02em}
  .contact b{font-weight:700}
</style>
</head>
<body>
  <div class="sheet-label">Design3</div>

  <section class="card card--front">
    <div class="photo-bg" role="img" aria-label="Foto: Hand massiert den Rücken einer entspannt liegenden Person"></div>

    <div class="title-panel brand">
      <div class="brand__owner">TOBIAS RENNERT</div>
      <div class="brand__service">HAWAIIANISCHE<br>MASSAGE &amp;<br>KÖRPERARBEIT</div>
    </div>

    <div class="badge badge--opening">PRAXIS<span>Eröffnung!</span></div>

    <div class="badge offer offer--lomi">
      <div class="offer__title">LOMI-LOMI<br>MASSAGE</div>
      <div class="offer__price">(90 Minuten) <b>95,– Euro</b></div>
      <div class="offer__note">(Lomi Ganzkörper-<br>massage – Gesamt-<br>dauer ca.2 Std.)</div>
    </div>

    <div class="badge offer offer--business">
      <div class="offer__title">BUSINESS-<br>MASSAGE</div>
      <div class="offer__price">(30 Minuten) <b>35,– Euro</b></div>
      <div class="offer__note">(z.B. für die Mittags-<br>pause – Gesamt-<br>dauer ca.45Min)</div>
    </div>

    <div class="promo-lead">Für Sie!</div>
    <div class="voucher voucher--front">erste Massage<br>zum<br>halber Preis</div>
  </section>

  <section class="card card--back">
    <div class="intro">
      <div class="intro__pre">Die hawaiianische</div>
      <div class="intro__title">LOMI LOMI MASSAGE <small>(oder Tempelmassage)</small></div>
      <p>ist eine Berührungskunst, welche von den Kahunas &nbsp;– den Wissensträgern –<br>bis heute praktiziert und weitergegeben wird.</p>
      <p>In der Massage wird der gesamte Körper unter Verwendung von hochwertigem<br>Massageöl mit Handballen und Unterarmen in langen, fließenden Bewegungen<br>massiert und ausgestrichen. Dadurch kann die Behandlung zu einer tiefen<br>Entspannung führen und Stress abbauen. Die Intensität und den Charakter<br>der Massage bestimmen dabei der Körper des Klienten und das Wesen des<br>Moments. Der Intimbereich bleibt dabei stets abgedeckt und unberührt.</p>
    </div>

    <div class="logo-block brand">
      <div class="brand__owner">TOBIAS RENNERT</div>
      <div class="brand__service">HAWAIIANISCHE<br>MASSAGE &amp;<br>KÖRPERARBEIT</div>
    </div>

    <div class="portrait" role="img" aria-label="Porträtfoto des Masseurs"></div>
    <div class="bio">
      <div class="bio__name">Tobias Rennert</div>
      Jahrgang 1979<br>
      Lomi Lomi Practitioner<br>
      (nach Kahu Keoni Lani)<br>
      Nalu-Kahuna-Bodywork Practitioner<br>
      Wellnessmasseur &amp; Wellnesstherapeut
    </div>

    <div class="bamboo" role="img" aria-label="Bambusstängel mit grünen Blättern"></div>

    <div class="reminder">Nicht vergessen!</div>
    <div class="voucher voucher--back">erste Massage<br>zum<br>halber Preis</div>
    <div class="appointments">Termine nach Vereinbarung!</div>

    <div class="contact"><b>Kontakt:</b> Lindenstiege 7 &nbsp;·&nbsp; 96047 Erlenbach (Eingang „Das Wohlfühlhaus“) &nbsp;·&nbsp; Telefon &nbsp;0951-480 372 16</div>
  </section>
</body>
</html>
```